4 sided DL flyer for a high end jewellery brand

I need a 4 sided DL flyer (21cm X 10cm) from my jewellery brand, ELUNE. My brand is UPSCALE and the flyer should be ELEGANT. I am uploading some sample images that can be used to create the flyer; however, I will get the final images in few days time. I am also attaching the following (1) My logo files - has the words ELUNE and icon (2) my business card - the front has the marble background that I am looking to use for the flyer and the logo style (gold foil). The back has the business details (3) mood board - blush pink/copper can also be used. Also please have space to write few lines about the brand and jewellery within the flyer. The flyer should be landscape.
Look and feel

```html
<!DOCTYPE html>
<html lang="en">
<head>
<meta charset="UTF-8">
<title>ELUNE – DL Flyer</title>
<link href="https://fonts.googleapis.com/css2?family=Josefin+Sans:wght@400;600&family=Open+Sans:wght@400;600&display=swap" rel="stylesheet">
<style>
  :root {
    --stage: #5c5c5c;
    --paper: #f7f7f7;
    --marble-light: #fbfbfb;
    --marble-vein: #dcdcdc;
    --gold: #c99a2e;
    --gold-deep: #b07f1c;
    --copper: #c5692a;
    --ink: #555555;
    --rule: #b9b9b9;
  }
  * { box-sizing: border-box; margin: 0; padding: 0; }
  html, body { width: 1200px; height: 1200px; overflow: hidden; }
  body {
    background: var(--stage);
    display: flex; align-items: center; justify-content: center;
    font-family: "Open Sans", sans-serif;
  }
  .spread { display: flex; width: 1080px; height: 540px; box-shadow: 0 12px 30px rgba(0,0,0,.35); }
  .panel {
    position: relative; width: 540px; height: 540px; overflow: hidden;
    background:
      radial-gradient(ellipse at 30% 25%, rgba(220,220,220,.55), transparent 45%),
      radial-gradient(ellipse at 75% 70%, rgba(215,215,215,.5), transparent 50%),
      radial-gradient(ellipse at 60% 15%, rgba(230,230,230,.6), transparent 40%),
      var(--marble-light);
  }
  .panel--inside { border-right: 1px solid #e6e6e6; }

  /* inside panel */
  .jewellery-photo {
    position: absolute; left: 40px; top: 20px; width: 460px; height: 230px;
    background: radial-gradient(ellipse at 55% 45%, rgba(214,196,220,.45), rgba(245,240,242,.2) 60%, transparent 80%);
  }
  .about { position: absolute; left: 40px; top: 262px; width: 460px; }
  .about__heading-row { display: flex; align-items: flex-end; gap: 10px; }
  .about__heading {
    font-family: "Josefin Sans", sans-serif; font-weight: 600; font-size: 20px; color: var(--copper);
  }
  .about__rule { flex: 1; height: 1px; background: var(--copper); opacity: .7; margin-bottom: 6px; }
  .about__text { margin-top: 6px; font-size: 11.5px; line-height: 1.45; color: var(--ink); }

  .contacts { position: absolute; left: 170px; top: 392px; display: flex; gap: 36px; font-size: 12px; color: var(--ink); }
  .contacts ul { list-style: none; display: flex; flex-direction: column; gap: 7px; }
  .contacts li { display: flex; align-items: center; gap: 8px; }
  .contacts svg { width: 13px; height: 13px; flex: none; }
  .dot { width: 12px; height: 12px; border-radius: 50%; background: var(--copper); flex: none; }

  .brand-mark-small {
    position: absolute; left: 40px; bottom: 36px;
    font-family: "Josefin Sans", sans-serif; font-weight: 400; font-size: 22px; letter-spacing: 6px; color: var(--gold);
  }

  /* cover panel */
  .brand-mark {
    position: absolute; top: 70px; left: 0; width: 100%; text-align: center;
    font-family: "Josefin Sans", sans-serif; font-weight: 400; font-size: 50px; letter-spacing: 16px; color: var(--gold);
  }
  .rings-photo {
    position: absolute; left: 110px; top: 160px; width: 320px; height: 190px; border-radius: 50%;
    background: linear-gradient(100deg, #e4e4e4 0%, #f2f2f2 42%, #e3c36f 58%, #c99a2e 100%);
  }
  .tagline {
    position: absolute; top: 390px; left: 0; width: 100%; text-align: center;
    font-family: "Josefin Sans", sans-serif; font-weight: 600; font-size: 40px; letter-spacing: 2px; color: var(--gold);
  }
  .web-row {
    position: absolute; top: 450px; left: 60px; right: 60px;
    display: flex; align-items: center; gap: 12px;
    font-size: 12px; letter-spacing: 4px; color: var(--ink);
  }
  .web-row span.line { flex: 1; height: 1px; background: var(--rule); }
</style>
</head>
<body>
<main class="spread">
  <section class="panel panel--inside">
    <div class="jewellery-photo" role="img" aria-label="Faded photograph of pendant necklaces and gemstone rings on marble"></div>

    <div class="about">
      <div class="about__heading-row">
        <h2 class="about__heading">About Us</h2>
        <span class="about__rule"></span>
      </div>
      <p class="about__text">Lorem Ipsum is simply dummy text of the printing and typesetting industry. Lorem Ipsum has been the industry's standard dummy text ever since the 1500s, when an unknown printer took a galley of type and scrambled it to make a type specimen book. It has survived not only five centuries, but also the leap into electronic typesetting, remaining essentially unchanged.</p>
    </div>

    <div class="contacts">
      <ul>
        <li>
          <svg viewBox="0 0 16 16"><path fill="var(--copper)" d="M3 1h3l1 4-2 1a9 9 0 0 0 5 5l1-2 4 1v3a2 2 0 0 1-2 2A13 13 0 0 1 1 3a2 2 0 0 1 2-2z"/></svg>
          +61400123456
        </li>
        <li>
          <svg viewBox="0 0 16 16"><rect x="1" y="3" width="14" height="10" rx="1" fill="var(--copper)"/><path d="M1 4l7 5 7-5" stroke="#fff" stroke-width="1.2" fill="none"/></svg>
          hello@elune.com.au
        </li>
        <li>
          <svg viewBox="0 0 16 16" fill="none" stroke="var(--copper)" stroke-width="1.3"><circle cx="8" cy="8" r="6.5"/><ellipse cx="8" cy="8" rx="3" ry="6.5"/><path d="M1.5 8h13"/></svg>
          www.elune.com.au
        </li>
      </ul>
      <ul>
        <li><span class="dot"></span>@elunejewellery</li>
        <li><span class="dot"></span>@elunejewellery</li>
        <li>ABN : 12345678901</li>
      </ul>
    </div>

    <div class="brand-mark-small">ELUNE</div>
  </section>

  <section class="panel panel--cover">
    <div class="brand-mark">ELUNE</div>
    <div class="rings-photo" role="img" aria-label="Photograph of a textured silver ring and a gold ring set with small diamonds"></div>
    <h1 class="tagline">LOVE IS IN THE AIR</h1>
    <div class="web-row"><span class="line"></span>www.elune.com.au<span class="line"></span></div>
  </section>
</main>
</body>
</html>
```